Comets Business Card Design Project

Create a standard format for letterhead and business cards. I know I can just get the layout with an example name on it, then add the names, titles and address that we want to it and give that to a printer so that the graphics are much better. Organization Mission Statement: Providing a professionally organized, structured, and supportive environment with quality development and professional coaching to inspire our student athletes, and assist them in fulfilling their dreams of achievement in academic excellence, high level competition and playing collegiate softball. Girl's Summit Windmill Softball

Check web site: www.bluecrestwindmillcomets.org
Updates

Sorry I didn't get the URL and files out when I started the project. Logo examples, mission, vision, etc. are posted now. And the URL to the web site is www.bluecrestwindmillcomets.org.

I'm very interested in an original creative design that is professional yet relevant to a sports team and for coaches.

Target Market(s)

college recuriters, industry product suppliers, parents, coaches, tournament directors

Industry/Entity Type

Environment

Requirements
Must have
• Use one of two logos; include the web site URL and a general mailbox for inquires. Includes Name, title, email and phone number
Nice to have
• Some color variations or background. Maybe a mission statement on the back. Maybe a QR code to the web site.

```html
<!DOCTYPE html>
<html lang="en">
<head>
<meta charset="utf-8">
<title>Bluecrest Comets Business Cards</title>
<link href="https://fonts.googleapis.com/css2?family=Cinzel:wght@500&family=Comfortaa:wght@400;700&display=swap" rel="stylesheet">
<style>
  :root {
    --backdrop: #1c1c1c;
    --card-light: #2b2b2b;
    --card-dark: #0b0b0b;
    --text-white: #f2f2f2;
    --brand-red: #e2334b;
    --brand-deep: #b52238;
    --divider: rgba(255,255,255,0.07);
  }
  * { margin: 0; padding: 0; box-sizing: border-box; }
  html, body {
    width: 1200px; height: 1000px; overflow: hidden;
    background: var(--backdrop);
  }
  .canvas { position: relative; width: 1200px; height: 1000px; }
  .card {
    position: absolute; left: 203px; width: 806px; height: 440px;
    background: radial-gradient(ellipse at 40% 35%, var(--card-light) 0%, #141414 55%, var(--card-dark) 100%);
    box-shadow: 0 6px 18px rgba(0,0,0,0.6);
    color: var(--text-white);
    font-family: "Comfortaa", sans-serif;
  }
  .card--front { top: 37px; }
  .card--alt { top: 521px; }
  .card__divider {
    position: absolute; left: 307px; top: 130px; width: 2px; height: 200px;
    background: linear-gradient(to bottom, transparent, var(--divider), transparent);
  }
  .team-name {
    position: absolute; left: 18px; top: 165px; width: 280px;
    font-family: "Comfortaa", sans-serif; font-weight: 700;
    font-size: 40px; line-height: 48px; text-align: center;
  }
  .card--front .team-name { color: var(--brand-red); }
  .card--alt .team-name { color: var(--brand-deep); }
  .person {
    position: absolute; left: 347px; top: 193px; width: 360px; text-align: right;
  }
  .person__name {
    font-family: "Cinzel", serif; font-weight: 500; font-size: 30px;
    line-height: 32px; letter-spacing: 0.5px; text-align: left;
  }
  .person__title {
    font-family: "Comfortaa", sans-serif; font-size: 11px;
    letter-spacing: 2.5px; line-height: 12px; margin-top: -2px;
  }
  .contact { position: absolute; left: 403px; top: 256px; list-style: none; }
  .contact li { font-size: 14px; line-height: 33.5px; letter-spacing: 0.3px; }
  .contact b { font-weight: 700; }
  .website {
    position: absolute; right: 10px; top: 416px;
    font-size: 12px; font-weight: 700; letter-spacing: 2.6px;
  }
</style>
</head>
<body>
<main class="canvas">
  <section class="card card--front">
    <div class="team-name">Bluecrest Comets</div>
    <div class="card__divider"></div>
    <div class="person">
      <h1 class="person__name">Dana Whitfield</h1>
      <p class="person__title">HEAD COACH</p>
    </div>
    <ul class="contact">
      <li><b>Phone:</b> 555 214 307</li>
      <li><b>Address:</b> 4120 Harbor Lane Oakridge, CA 90415</li>
      <li><b>Email:</b> coach@bluecrestcomets.org</li>
    </ul>
    <p class="website">WWW.BLUECRESTWINDMILLCOMETS.ORG</p>
  </section>

  <section class="card card--alt">
    <div class="team-name">Bluecrest Comets</div>
    <div class="card__divider"></div>
    <div class="person">
      <h2 class="person__name">Dana Whitfield</h2>
      <p class="person__title">HEAD COACH</p>
    </div>
    <ul class="contact">
      <li><b>Phone:</b> 555 214 307</li>
      <li><b>Address:</b> 4120 Harbor Lane Oakridge, CA 90415</li>
      <li><b>Email:</b> coach@bluecrestcomets.org</li>
    </ul>
    <p class="website">WWW.BLUECRESTWINDMILLCOMETS.ORG</p>
  </section>
</main>
</body>
</html>
```